Twitch Streamer Needs a Business Card Design

I need a business card design for my Twitch stream. It's a channel that plays a variety of games but has a modern royal theme with purple, black and gold as the main colors. Font should be easily readable but have a bit of flair to it to make it stand out/be unique. Should be a bit edgy and funky, but maintain the royal theme. Only standard shaped business cards please.
Updates

- Name on the card should read Wendel Pashby, not Duke Varlosk- Would like to see designs with and without Duke Varlosk on the back with the logo Added Sunday, February 22, 2015

Target Market(s)

Game Developers and product makers

Industry/Entity Type

Games

Contact Information for Business Card

I would like to have the logo on the back. Contact info I need on the card would be my phone number, Twitch, Twitter, email, and YouTube.

Requirements
Must have
• Name: Duke Varlosk
• Phone Number: 401-555-0178
• Twitch: streamhall.tv/dukevarlosk
• Twitter: @DukeVarlosk
• Email: dukevarlosk@mailvexa.com
• YouTube: Duke Varlosk
• Logo on the back
• "Duke Varlosk" below logo
Nice to have
• Font should be easily readable but have a small bit of unique flair.

```html
<!DOCTYPE html>
<html lang="en">
<head>
<meta charset="utf-8">
<title>Duke Varlosk – Business Cards</title>
<link rel="stylesheet" href="https://fonts.googleapis.com/css2?family=Cinzel:wght@400;600&family=Michroma&family=Raleway:wght@400&family=Almendra:ital,wght@1,700&display=swap">
<style>
  :root {
    --stage: #ffffff;
    --card-top: #1d1d1f;
    --card-bottom: #0a0a0b;
    --gold: #c99a2e;
    --gold-light: #e2b956;
    --royal-purple: #5b2a86;
    --text-light: #f1f1f1;
    --text-muted: #b9b9b9;
    --icon-grey: #8a8a8a;
    --label-ink: #111111;
  }
  * { box-sizing: border-box; margin: 0; padding: 0; }
  html, body { width: 1200px; height: 800px; overflow: hidden; background: var(--stage); }
  .stage { position: relative; width: 1200px; height: 800px; }

  .card {
    position: absolute;
    width: 525px; height: 300px;
    border-radius: 14px;
    background: radial-gradient(ellipse at 40% 30%, var(--card-top), var(--card-bottom) 80%);
    overflow: hidden;
    box-shadow: 0 6px 18px rgba(0,0,0,.25);
  }

  /* Front */
  .card--front { left: 40px; top: 250px; }
  .front__rule { position: absolute; left: 0; right: 0; top: 272px; height: 2px; background: var(--gold); }
  .front__divider { position: absolute; left: 208px; top: 40px; width: 2px; height: 200px; background: var(--gold); }
  .brand-mark {
    position: absolute; display: flex; align-items: center; gap: 10px;
    font-family: "Cinzel", serif; font-weight: 600; color: var(--gold-light);
  }
  .brand-mark__dot { width: 34px; height: 34px; border-radius: 50%; background: var(--royal-purple); flex: none; }
  .front__brand { left: 26px; top: 120px; font-size: 17px; }
  .front__details { position: absolute; left: 230px; top: 46px; }
  .front__name {
    font-family: "Michroma", sans-serif; font-size: 19px; letter-spacing: 1px;
    color: var(--text-light); margin-bottom: 16px; text-transform: uppercase;
  }
  .contact-list { list-style: none; }
  .contact-list li {
    display: flex; align-items: center; gap: 10px;
    font-family: "Raleway", sans-serif; font-size: 13px; color: var(--text-muted);
    line-height: 26px;
  }
  .contact-icon { width: 14px; height: 14px; flex: none; }
  .contact-icon--dot { border-radius: 50%; background: var(--icon-grey); }

  /* Backs */
  .card--back-plain { left: 635px; top: 90px; }
  .card--back-logo { left: 635px; top: 430px; }
  .back__band { position: absolute; top: 0; bottom: 0; width: 5px; background: var(--gold); }
  .back__band--left { left: 42px; }
  .back__band--right { right: 42px; }
  .back__halo {
    position: absolute; left: 50%; top: 50%; width: 110px; height: 110px;
    margin: -55px 0 0 -55px; border-radius: 50%; background: var(--royal-purple); opacity: .35;
  }
  .back__title {
    position: absolute; inset: 0; display: flex; align-items: center; justify-content: center;
    font-family: "Cinzel", serif; font-size: 40px; letter-spacing: 2px; color: var(--gold);
  }
  .back-logo__brand { left: 50%; top: 70px; transform: translateX(-50%); font-size: 18px; white-space: nowrap; }
  .back-logo__script {
    position: absolute; left: 0; right: 0; top: 160px; text-align: center;
    font-family: "Almendra", serif; font-style: italic; font-weight: 700;
    font-size: 44px; color: var(--gold);
  }

  .option-label {
    position: absolute; font-family: "Raleway", sans-serif; font-size: 72px; color: var(--label-ink);
  }
  .option-label--one { left: 585px; top: 70px; }
  .option-label--two { left: 585px; top: 410px; }
</style>
</head>
<body>
<main class="stage">

  <section class="card card--front" aria-label="Card front">
    <div class="brand-mark front__brand"><span class="brand-mark__dot"></span>Duke Varlosk</div>
    <div class="front__divider"></div>
    <div class="front__details">
      <h1 class="front__name">Wendel Pashby</h1>
      <ul class="contact-list">
        <li>
          <svg class="contact-icon" viewBox="0 0 14 14" aria-hidden="true"><path d="M3 1h3l1 3-2 1.5a8 8 0 0 0 3.5 3.5L10 7l3 1v3a2 2 0 0 1-2 2A10 10 0 0 1 1 3a2 2 0 0 1 2-2z" fill="var(--icon-grey)"/></svg>
          401-555-0178
        </li>
        <li>
          <svg class="contact-icon" viewBox="0 0 14 14" aria-hidden="true"><rect x="1" y="3" width="12" height="8" rx="1" fill="none" stroke="var(--icon-grey)" stroke-width="1.3"/><path d="M1.5 3.5 7 8l5.5-4.5" fill="none" stroke="var(--icon-grey)" stroke-width="1.3"/></svg>
          dukevarlosk@mailvexa.com
        </li>
        <li><span class="contact-icon contact-icon--dot"></span>@DukeVarlosk</li>
        <li><span class="contact-icon contact-icon--dot"></span>Duke Varlosk</li>
        <li><span class="contact-icon contact-icon--dot"></span>streamhall.tv/dukevarlosk</li>
      </ul>
    </div>
    <div class="front__rule"></div>
  </section>

  <span class="option-label option-label--one">1</span>
  <section class="card card--back-plain" aria-label="Card back, option one">
    <div class="back__band back__band--left"></div>
    <div class="back__band back__band--right"></div>
    <div class="back__halo"></div>
    <p class="back__title">DUKE VARLOSK</p>
  </section>

  <span class="option-label option-label--two">2</span>
  <section class="card card--back-logo" aria-label="Card back, option two">
    <div class="back__band back__band--left"></div>
    <div class="back__band back__band--right"></div>
    <div class="brand-mark back-logo__brand"><span class="brand-mark__dot"></span>Duke Varlosk</div>
    <p class="back-logo__script">Duke Varlosk</p>
  </section>

</main>
</body>
</html>
```